A Maple Syrup Label for a Local Buniness

We are looking for a label for our maple syrup business. Our business currently sells honey, and we are expanding into maple syrup. Our Business name is "Corvale Bees" and we currently have a logo attached below. We would like to incorporate the bee and CB part, but the label could also read "Corvale Farms" with the words maple syrup. We do not want consumers to confuse the maple syrup jars with the honey jars. It should be clear that the jars contain maple syrup. We are open to new designs as well.

```html
<!DOCTYPE html>
<html lang="en">
<head>
<meta charset="utf-8">
<title>Corvale Maple Syrup Label</title>
<link rel="stylesheet" href="https://fonts.googleapis.com/css2?family=Open+Sans:wght@400;700;800&family=Playfair+Display:wght@500&family=Tinos&display=swap">
<style>
  :root {
    --paper: #ffffff;
    --cream: #fcf4ea;
    --cream-band: #f9ebd9;
    --maple-red: #ae2418;
    --wine: #8b1820;
    --pewter: #858079;
    --bark: #5e3a27;
    --ink: #141414;
    --slate: #333333;
    --edge: #444444;
  }
  html, body {
    margin: 0;
    padding: 0;
    width: 1200px;
    height: 822px;
    overflow: hidden;
    background: var(--paper);
  }
  .label-sheet {
    display: block;
    width: 1200px;
    height: 822px;
    box-sizing: border-box;
    border: 1px solid var(--edge);
  }
  .frame-outer { fill: var(--cream); stroke: var(--maple-red); stroke-width: 8; stroke-linejoin: round; }
  .frame-pewter { fill: none; stroke: var(--pewter); stroke-width: 12; }
  .frame-bark { fill: none; stroke: var(--bark); stroke-width: 7; }
  .frame-inner { fill: none; stroke: var(--maple-red); stroke-width: 4; }
  .band { fill: var(--cream-band); }
  .brand-title {
    font-family: "Playfair Display", serif;
    font-weight: 500;
    font-size: 150px;
    fill: var(--ink);
    stroke: var(--ink);
    stroke-width: 2;
  }
  .product-name {
    font-family: "Open Sans", sans-serif;
    font-weight: 800;
    font-size: 92px;
    fill: var(--wine);
  }
  .emblem-mark { fill: var(--maple-red); }
  .emblem-name {
    font-family: "Open Sans", sans-serif;
    font-weight: 700;
    font-size: 44px;
    fill: var(--maple-red);
  }
  .producer-text {
    font-family: "Open Sans", sans-serif;
    font-weight: 400;
    font-size: 31px;
    fill: var(--slate);
  }
  .producer-name { font-weight: 700; font-size: 34px; fill: var(--wine); }
  .ingredients-text {
    font-family: "Open Sans", sans-serif;
    font-size: 27px;
    fill: var(--slate);
  }
  .ingredients-heading { font-weight: 700; }
  .french-name, .volume {
    font-family: "Tinos", serif;
    font-size: 31px;
    fill: var(--slate);
  }
  .arc-tagline {
    font-family: "Open Sans", sans-serif;
    font-weight: 700;
    font-size: 30px;
    fill: var(--slate);
  }
</style>
</head>
<body>
<svg class="label-sheet" viewBox="0 0 2324 1591" width="1200" height="822" preserveAspectRatio="none" xmlns="http://www.w3.org/2000/svg">
  <defs>
    <clipPath id="label-body">
      <path d="M265,497 L678,497 C705,497 722,485 735,463 C860,262 1010,187 1162,187 C1314,187 1464,262 1589,463 C1602,485 1619,497 1646,497 L2058,497 L2058,1094 L1646,1094 C1619,1094 1602,1106 1589,1128 C1464,1329 1314,1404 1162,1404 C1010,1404 860,1329 735,1128 C722,1106 705,1094 678,1094 L265,1094 Z"/>
    </clipPath>
    <path id="tagline-arc" d="M850,1238 Q1160,1500 1478,1232"/>
  </defs>

  <path class="frame-outer" d="M205,436 L675,436 C820,190 1000,125 1162,125 C1324,125 1504,190 1648,436 L2118,436 L2118,1155 L1648,1155 C1504,1400 1324,1467 1162,1467 C1000,1467 820,1400 675,1155 L205,1155 Z"/>

  <g clip-path="url(#label-body)">
    <rect class="band" x="0" y="152" width="2324" height="70"/>
    <rect class="band" x="0" y="304" width="2324" height="70"/>
    <rect class="band" x="0" y="457" width="2324" height="70"/>
    <rect class="band" x="0" y="609" width="2324" height="70"/>
    <rect class="band" x="0" y="761" width="2324" height="70"/>
    <rect class="band" x="0" y="913" width="2324" height="70"/>
    <rect class="band" x="0" y="1065" width="2324" height="70"/>
    <rect class="band" x="0" y="1217" width="2324" height="70"/>
    <rect class="band" x="0" y="1369" width="2324" height="70"/>
  </g>

  <path class="frame-pewter" d="M229,460 L680,460 C694,460 703,454 710,442 C845,212 1005,150 1162,150 C1319,150 1479,212 1614,442 C1621,454 1630,460 1644,460 L2094,460 L2094,1131 L1644,1131 C1630,1131 1621,1137 1614,1149 C1479,1379 1319,1442 1162,1442 C1005,1442 845,1379 710,1149 C703,1137 694,1131 680,1131 L229,1131 Z"/>
  <path class="frame-bark" d="M252,483 L680,483 C700,483 712,474 721,459 C855,238 1008,174 1162,174 C1316,174 1469,238 1603,459 C1612,474 1624,483 1644,483 L2071,483 L2071,1108 L1644,1108 C1624,1108 1612,1117 1603,1132 C1469,1353 1316,1418 1162,1418 C1008,1418 855,1353 721,1132 C712,1117 700,1108 680,1108 L252,1108 Z"/>
  <path class="frame-inner" d="M265,497 L678,497 C705,497 722,485 735,463 C860,262 1010,187 1162,187 C1314,187 1464,262 1589,463 C1602,485 1619,497 1646,497 L2058,497 L2058,1094 L1646,1094 C1619,1094 1602,1106 1589,1128 C1464,1329 1314,1404 1162,1404 C1010,1404 860,1329 735,1128 C722,1106 705,1094 678,1094 L265,1094 Z"/>

  <g class="emblem" role="img" aria-label="Corvale Bees emblem">
    <circle class="emblem-mark" cx="1162" cy="440" r="42"/>
    <text class="emblem-name" x="1162" y="560" text-anchor="middle">Corvale Bees</text>
  </g>

  <text class="brand-title" x="1162" y="815" text-anchor="middle" textLength="833" lengthAdjust="spacing">CORVALE</text>
  <text class="product-name" x="1162" y="908" text-anchor="middle" textLength="773" lengthAdjust="spacing">MAPLE SYRUP</text>

  <g class="producer" transform="translate(0,798)">
    <text class="producer-text" transform="translate(480,0) rotate(90)" text-anchor="middle">Produced by:</text>
    <text class="producer-text producer-name" transform="translate(425,0) rotate(90)" text-anchor="middle">Corvale Bees</text>
    <text class="producer-text" transform="translate(381,0) rotate(90)" text-anchor="middle">217 Birchline Road</text>
    <text class="producer-text" transform="translate(334,0) rotate(90)" text-anchor="middle">Alderbrook ON K0A 2Z0.</text>
  </g>

  <g class="ingredients">
    <text class="ingredients-text" transform="translate(1812,1062) rotate(-90)" textLength="466" lengthAdjust="spacingAndGlyphs"><tspan class="ingredients-heading">Ingredients:</tspan> dolor sit amet, consectur</text>
    <text class="ingredients-text" transform="translate(1849,1062) rotate(-90)" textLength="498" lengthAdjust="spacingAndGlyphs">adipiscing elit. Phasellus sodales malesuada</text>
    <text class="ingredients-text" transform="translate(1886,1062) rotate(-90)" textLength="470" lengthAdjust="spacingAndGlyphs">est, vitae suscipit nunc faucibus in. Sed ac</text>
    <text class="ingredients-text" transform="translate(1922,1062) rotate(-90)" textLength="445" lengthAdjust="spacingAndGlyphs">accumsan risus, vel sodales risus. Nulla.</text>
  </g>

  <text class="french-name" x="1172" y="1246" text-anchor="middle">SIROP D'ÉRABLE</text>
  <text class="volume" x="1172" y="1288" text-anchor="middle">500 ml</text>
  <text class="arc-tagline"><textPath href="#tagline-arc" startOffset="50%" text-anchor="middle">PURE ONTARIO MAPLE SYRUP • SMALL BATCHES</textPath></text>
</svg>
</body>
</html>
```